An international wholesale business needs letterhead design

Logo file is attached. Please design a letterhead with the following details:

- Company Name and Logo
- Address
- VAT Registration number
- Phone No
- Website address

```html
<!DOCTYPE html>
<html lang="en">
<head>
<meta charset="utf-8">
<title>Korven Trading Letterhead</title>
<link rel="stylesheet" href="https://fonts.googleapis.com/css2?family=Arimo:wght@400;700&family=Mulish:wght@700;800&display=swap">
<style>
  :root {
    --backdrop: #acaaab;
    --paper: #ffffff;
    --brand-red: #c6252d;
    --ink: #4d4d4f;
    --muted: #8a8c8f;
    --rule: #9a9a9a;
  }
  * { margin: 0; padding: 0; box-sizing: border-box; }
  html, body {
    width: 1200px; height: 934px; overflow: hidden;
    background: var(--backdrop);
  }
  .letterhead {
    position: absolute; left: 313px; top: 60px;
    width: 574px; height: 813px;
    background: var(--paper);
    font-family: "Arimo", Arial, sans-serif;
    color: var(--ink);
  }
  .brand {
    position: absolute; left: 51px; top: 62px;
    width: 196px;
  }
  .brand-name {
    font-family: "Arimo", Arial, sans-serif;
    font-weight: 700; font-size: 20px; letter-spacing: 0.4px;
    line-height: 28px; white-space: nowrap;
    color: var(--brand-red);
  }
  .contact {
    position: absolute; left: 408px; top: 34px; height: 84px;
    border-left: 1px solid var(--rule);
    padding-left: 10px;
    font-style: normal;
    font-size: 9.2px; line-height: 12px; color: var(--muted);
  }
  .contact .vat-label { color: var(--brand-red); font-weight: 700; }
  .contact .address { margin-top: 6px; }
  .contact .channels { margin-top: 7px; list-style: none; }
  .contact .channels li { display: flex; align-items: center; gap: 6px; }
  .contact svg { width: 7px; height: 7px; flex: none; }
  .salutation {
    position: absolute; left: 52px; top: 248px;
    font-family: "Mulish", sans-serif; font-weight: 800;
    font-size: 13.2px; color: var(--ink);
  }
  .body-copy {
    position: absolute; left: 51px; top: 288px; width: 480px;
    font-size: 9.9px; line-height: 11.8px; white-space: nowrap;
  }
  .body-copy p + p { margin-top: 10.2px; }
  .closing {
    position: absolute; left: 52px; top: 532px;
    font-family: "Mulish", sans-serif; font-weight: 800; font-size: 8px;
  }
  .signature {
    position: absolute; left: 51px; top: 564px;
    width: 96px; height: 30px;
    background: linear-gradient(90deg, #e4e4e5, #f1f1f2);
    border-radius: 3px;
  }
</style>
</head>
<body>
  <main class="letterhead">
    <header>
      <div class="brand">
        <span class="brand-name">KORVEN TRADING</span>
      </div>
      <address class="contact">
        <div><span class="vat-label">VAT:</span> 12345678900</div>
        <div class="address">Your address, city<br>state, ZIP 0000</div>
        <ul class="channels">
          <li><svg viewBox="0 0 10 10"><path d="M2 1l2 2-1 1.3c.6 1.2 1.5 2.1 2.7 2.7L7 6l2 2-1.4 1.5C4.5 9 1 5.5.5 2.4z" fill="#c6252d"/></svg>123-456-2100</li>
          <li><svg viewBox="0 0 10 10"><rect x="0.7" y="2" width="8.6" height="6" fill="none" stroke="#c6252d" stroke-width="1"/><path d="M.7 2L5 5.5 9.3 2" fill="none" stroke="#c6252d" stroke-width="1"/></svg>youremail@gmail.com</li>
          <li><svg viewBox="0 0 10 10"><g fill="none" stroke="#c6252d" stroke-width=".9"><circle cx="5" cy="5" r="4.3"/><ellipse cx="5" cy="5" rx="1.8" ry="4.3"/><path d="M.7 5h8.6M1.5 2.8h7M1.5 7.2h7"/></g></svg>www.yourwebsite.com</li>
        </ul>
      </address>
    </header>

    <h1 class="salutation">Dear Mr. Smith,</h1>

    <section class="body-copy">
      <p>Lorem ipsum dolor sit amet, consectetuer adipiscing elit, sed diam nonmmy nibh euismod tincidunt ut laor<br>eet dolore magna aliquam erat volutpat. Ut wisi enim ad minim veniam, quis nostrud exerci tationmcorper<br>suscipit lobortis nisl ut aliquip ex ea commodo consequat. Duis autem vel eum iriure dolor in hendrerit in<br>vulputate velit esse molestie consequat, vel illum dolore eu feugiat</p>
      <p>Rorem ipsum dolor sit amet, consectetuer adipiscing elit, sed diam nonmmy nibh euismod tincidunt ut laor<br>eet dolore magna aliquam erat volutpat. Ut wisi enim ad minim veniam, quis nostrud exerci tationmcorper<br>suscipit lobortis nisl ut aliquip ex ea commodo consequat. Duis autem vel eum iriure dolor in hendrerit in<br>vulputate velit esse molest</p>
      <p>Dorem ipsum dolor sit amet, consectetuer adipiscing elit, sed diam nonmmy nibh euismod tincidunt ut laor<br>eet dolore magna aliquam erat volutpat. Ut wisi enim ad minim veniam, quis nostrud exerci tationmcorper<br>suscipit lobortis nisl ut aliquip ex ea commodo consequat. Duis autem vel eum iriure dolor in hendrerit in<br>suscipit lobortis nisl ut aliquip ex ea commodo consequat. Duis autem vel eum iriure dolor in hendrerit in<br>vulputate velit esse molestie consequat, vel illum</p>
      <p>Sorem ipsum dolor sit amet, consectetuer adipiscing elit, sed diam nonmmy nibh euismod tincidunt ut laor<br>eet dolore magna aliquam erat volutpat. Ut wisi enim ad minim veniam, quis nostrud exerci tationmcorper<br>suscipit lobortis nisl ut aliquip ex ea commodo consequat. Duis autem vel eum iriure dolor in</p>
    </section>

    <p class="closing">Sincerely,</p>
    <div class="signature" role="img" aria-label="Handwritten signature of the sender"></div>
  </main>
</body>
</html>
```